Personal Letterhead - Vintage / Antique - Foil Pressed

I need a personal letterhead. I'm an engineer and maker who enjoys writing letters and calligraphy. The final design will be foil pressed with either gold or copper foil. I'm going for an antique and vintage look. Something akin to Walter Brisbane's letterhead. Please include a spot for a web address and email, each are 16 characters long. The primary name to include is Daniel Harper. You can include print elements if desired that will be separate from the foil elements. At your discretion, you may or may not include the Harper signature I attached. It is optional depending on how well it meshes with your design.
I, explicitly, am not just looking for my name in gold or copper at the top of the page. I'm looking for additional design elements that give a similar feeling to the example design provided.

```html
<!DOCTYPE html>
<html lang="en">
<head>
<meta charset="utf-8">
<title>Daniel Harper — Letterhead</title>
<link rel="stylesheet" href="https://fonts.googleapis.com/css2?family=Rye&family=Cinzel:wght@700&display=swap">
<style>
  :root {
    --paper-light: #efe3c3;
    --paper-mid: #e8d6ac;
    --paper-warm: #e2c999;
    --foil: #9c7650;
  }
  html, body {
    margin: 0;
    padding: 0;
    overflow: hidden;
    background: var(--paper-light);
  }
  .letterhead {
    position: relative;
    width: 927px;
    height: 1200px;
    overflow: hidden;
    background:
      radial-gradient(ellipse at 30% 55%, rgba(255,255,255,0.25), transparent 60%),
      radial-gradient(ellipse at 85% 70%, rgba(214,180,120,0.35), transparent 55%),
      radial-gradient(ellipse at 15% 95%, rgba(205,165,105,0.4), transparent 45%),
      linear-gradient(180deg, var(--paper-light) 0%, var(--paper-mid) 60%, var(--paper-warm) 100%);
  }
  .frame-art {
    position: absolute;
    inset: 0;
  }
  .name {
    position: absolute;
    top: 88px;
    left: 0;
    width: 927px;
    margin: 0;
    text-align: center;
    font-family: "Rye", serif;
    font-weight: 400;
    font-size: 60px;
    letter-spacing: 6px;
    color: var(--foil);
    line-height: 1;
  }
  .contact-label {
    position: absolute;
    top: 1101px;
    margin: 0;
    font-family: "Cinzel", serif;
    font-weight: 700;
    font-size: 13px;
    letter-spacing: 1px;
    color: var(--foil);
  }
  .contact-label--web { left: 74px; }
  .contact-label--email { left: 553px; }
</style>
</head>
<body>
<main class="letterhead">
  <svg class="frame-art" width="927" height="1200" viewBox="0 0 927 1200" aria-hidden="false">
    <!-- header rules -->
    <g class="header-rules" fill="var(--foil)">
      <polygon points="198,79 350,75 420,78 350,81"/>
      <polygon points="733,79 580,75 510,78 580,81"/>
      <polygon points="198,175 350,172 420,175 350,178"/>
      <polygon points="733,175 580,172 510,175 580,178"/>
    </g>
    <rect class="header-ornament" role="img" aria-label="Scrolled flourish with star crowning the name" x="348" y="28" width="234" height="50" rx="20" fill="var(--foil)" opacity="0.35"/>
    <rect class="footer-ornament" role="img" aria-label="Scrolled flourish with star beneath the name" x="370" y="176" width="190" height="32" rx="14" fill="var(--foil)" opacity="0.35"/>

    <!-- footer contact bar -->
    <g class="contact-bar" fill="none" stroke="var(--foil)">
      <line x1="169" y1="1070" x2="760" y2="1070" stroke-width="2.5"/>
      <line x1="169" y1="1148" x2="760" y2="1148" stroke-width="2.5"/>
      <rect x="58" y="1077" width="813" height="63" stroke-width="2"/>
    </g>
    <g class="seal">
      <circle cx="461" cy="1109" r="74" fill="var(--paper-mid)" stroke="var(--foil)" stroke-width="2"/>
      <circle cx="461" cy="1109" r="66" fill="none" stroke="var(--foil)" stroke-width="1.5"/>
      <circle role="img" aria-label="Handwritten Harper signature" cx="461" cy="1109" r="58" fill="var(--foil)" opacity="0.12"/>
    </g>
  </svg>

  <h1 class="name">Daniel Harper</h1>
  <p class="contact-label contact-label--web">WEB :</p>
  <p class="contact-label contact-label--email">EMAIL :</p>
</main>
</body>
</html>
```